Rivet Halvora needs a new Website Design

We need a WEB site landing page (/template) design, we currently have a company logo.We like the Tarvex.com web designEnclosed is our company logo.Our Current website is https://www.rivethalvora.com.au/

Number of Pages Required

1 page

```html
<!DOCTYPE html>
<html lang="en">
<head>
<meta charset="utf-8">
<title>Halvora UC — Unified Communications</title>
<link href="https://fonts.googleapis.com/css2?family=Roboto:wght@300;400;500;700&family=Raleway:wght@400;500;700&display=swap" rel="stylesheet">
<style>
:root{
  --ink:#2d2d2d;
  --muted:#8a8f96;
  --faint:#b9bec4;
  --blue:#1e7fd0;
  --brand:#2a9fd8;
  --line:#e9ecef;
  --sky:#7fcdfc;
  --navy:#061428;
  --teal:#1fc6d6;
  --foot:#f7f9fb;
  --white:#ffffff;
}
*{box-sizing:border-box;margin:0;padding:0}
html,body{width:1200px;height:2203px;overflow:hidden;background:var(--white)}
body{font-family:"Roboto",sans-serif;color:var(--ink)}
.page{position:relative;width:1200px;height:2203px;overflow:hidden}
.abs{position:absolute}

/* top bar */
.topbar{left:0;top:0;width:1200px;height:25px;border-bottom:1px solid var(--line)}
.socials{left:243px;top:8px;display:flex;gap:14px}
.socials span{width:8px;height:8px;border-radius:50%;background:#c4c8cd;display:block}
.hotline{right:243px;top:8px;font-size:7.5px;color:var(--muted)}
.hotline b{color:var(--ink);font-weight:500;margin-right:8px}

/* nav */
.nav{left:0;top:25px;width:1200px;height:43px;box-shadow:0 2px 6px rgba(0,0,0,.05);background:var(--white);z-index:2}
.logo{display:flex;align-items:center;gap:6px;font-family:"Roboto",sans-serif;font-weight:300;color:var(--brand)}
.logo i{display:block;border-radius:50%;background:var(--brand)}
.nav .logo{position:absolute;left:222px;top:10px;font-size:19px}
.nav .logo i{width:10px;height:10px}
.menu{position:absolute;right:243px;top:0;display:flex;gap:31px;height:43px;align-items:center}
.menu a{font-size:7.5px;letter-spacing:1.6px;color:#555;text-decoration:none;position:relative;height:43px;line-height:46px}
.menu a.on::before{content:"";position:absolute;left:-4px;right:-4px;top:0;height:1.5px;background:#3cb371}
.burger{width:9px;display:flex;flex-direction:column;gap:2px}
.burger span{height:1px;background:#444;display:block}

/* hero */
.hero{left:0;top:68px;width:1200px;height:489px;background:linear-gradient(180deg,#f6f6f7 0%,#f1f2f3 70%,#e9eaec 100%)}
.hero h1{position:absolute;left:0;width:1200px;top:185px;text-align:center;font-weight:300;font-size:37px;line-height:45px;color:#333}
.hero p{position:absolute;left:380px;width:440px;top:294px;text-align:center;font-size:11px;line-height:16.5px;color:#444;font-weight:300}
.btn{display:inline-block;background:var(--blue);color:var(--white);border-radius:14px;text-align:center}
.hero .btn{position:absolute;left:556px;top:350px;width:87px;height:27px;line-height:27px;font-size:8.5px}

/* about */
.device{left:0;top:655px;width:420px;height:378px;background:#f3f3f3;border-radius:0 10px 0 0}
.device .screen{position:absolute;left:0;top:26px;width:396px;height:322px;background:linear-gradient(135deg,#2a80b3,#1e6e9f)}
.device .base{position:absolute;left:0;top:378px;width:490px;height:12px;background:linear-gradient(#f0f0f0,#dedede);border-radius:0 0 40px 0;box-shadow:0 10px 18px rgba(0,0,0,.08)}
.about-h{left:480px;top:640px;font-size:15.5px;font-weight:300;color:#333}
.about-p{left:480px;top:671px;width:390px;font-size:7.8px;line-height:15px;color:var(--muted);font-weight:300}
.feat{width:235px;height:70px}
.feat svg{position:absolute;left:0;top:10px}
.feat .rule{position:absolute;left:39px;top:0;width:1px;height:55px;background:var(--line)}
.feat h4{position:absolute;left:56px;top:0;font-family:"Raleway",sans-serif;font-size:7.5px;font-weight:500;letter-spacing:.3px;color:#333}
.feat p{position:absolute;left:56px;top:20px;width:170px;font-size:7.8px;line-height:15px;color:var(--muted);font-weight:300}

/* services */
.services{left:0;top:1172px;width:1200px;height:649px;background:radial-gradient(ellipse at 80% 30%,#0f5f6e 0%,#08283a 40%,var(--navy) 75%)}
.services h2{position:absolute;left:0;width:1200px;top:48px;text-align:center;font-family:"Raleway",sans-serif;font-weight:700;font-size:16px;color:var(--white)}
.services .sub{position:absolute;left:0;width:1200px;top:73px;text-align:center;font-family:"Raleway",sans-serif;font-size:9.5px;color:var(--white)}
.svc{left:243px;width:230px;color:var(--white);font-family:"Raleway",sans-serif}
.svc svg{position:absolute;left:0;top:0}
.svc h3{position:absolute;left:46px;top:3px;font-size:8.5px;font-weight:700;letter-spacing:-.1px}
.svc p{position:absolute;left:46px;top:19px;width:180px;font-size:8.8px;line-height:15px}
.screens{left:572px;top:1318px;width:418px;height:312px}
.tablet{position:absolute;left:198px;top:0;width:220px;height:312px;background:var(--white);border-radius:8px}
.tablet .scr{position:absolute;left:12px;top:27px;width:196px;height:258px;background:linear-gradient(180deg,#f4d32a 0%,#f4d32a 52%,#d6d6d6 52%)}
.laptop{position:absolute;left:0;top:83px;width:310px;height:220px;background:var(--white);border-radius:8px;border:1px solid #ddd}
.laptop .scr{position:absolute;left:26px;top:12px;width:258px;height:196px;background:linear-gradient(180deg,#eef3f8,#dfe7ef);border:1px solid #444}

/* cta */
.cta{left:0;top:1821px;width:1200px;height:132px;background:var(--sky)}
.cta h2{position:absolute;left:244px;top:46px;font-weight:300;font-size:29px;color:#1d2b36}
.cta .btn{position:absolute;left:841px;top:48px;width:149px;height:30px;line-height:30px;font-size:15px;border-radius:15px}

/* footer */
.footer{left:0;top:1953px;width:1200px;height:250px;background:var(--foot)}
.footer .logo{position:absolute;left:214px;top:40px;font-size:18px}
.footer .logo i{width:10px;height:10px}
.about-f{position:absolute;left:214px;top:85px;width:220px;font-size:8px;line-height:15px;color:var(--muted);font-weight:300}
.legal{position:absolute;left:214px;top:167px;display:flex;gap:23px;font-size:7px;letter-spacing:1.1px;color:#333}
.copy{position:absolute;left:214px;top:190px;font-size:7.5px;color:var(--faint)}
.col{position:absolute;top:51px}
.col h5{font-size:8px;font-weight:400;letter-spacing:.3px;color:#333;margin-bottom:18px}
.col li{list-style:none;font-size:8px;line-height:21.3px;color:var(--faint);font-weight:300}
.col.dark li{color:#666}
.field{width:167px;height:23px;background:var(--white);border:1px solid #e1e4e8;font-size:6.5px;color:#777;padding:7px 6px;margin-bottom:1px}
.field.msg{height:53px}
.send{display:block;margin-top:8px;width:52px;height:27px;line-height:27px;font-size:8px;border-radius:14px}
</style>
</head>
<body>
<div class="page">

  <div class="abs topbar">
    <div class="abs socials"><span></span><span></span><span></span><span></span><span></span><span></span></div>
    <div class="abs hotline"><b>Hot Line</b>+1 555 0142 800</div>
  </div>

  <header class="abs nav">
    <div class="logo"><i></i>Halvora UC</div>
    <nav class="menu">
      <a class="on">HOME</a><a>ABOUT</a><a>SERVICES</a><a>BLOG</a><a>TERMS</a><a>CONTACT US</a>
      <div class="burger"><span></span><span></span><span></span></div>
    </nav>
  </header>

  <section class="abs hero" role="img" aria-label="Faded illustration of call centre agents with headsets at laptops under coloured speech bubbles">
    <h1>Australia's Business Grade Unified<br>Communications Company</h1>
    <p>Lorem ipsum dolor sit amet, consectetuer adipiscing elit. Aenean commodo ligula eget dolor. Aenean massa. Cum sociis penatibus et magnis.</p>
    <span class="btn">Contact Us</span>
  </section>

  <div class="abs device">
    <div class="screen" role="img" aria-label="Isometric illustration of connected devices, cloud, globe and messaging icons"></div>
    <div class="base"></div>
  </div>
  <h2 class="abs about-h">We have all the components to start and run your own White Label Telco</h2>
  <p class="abs about-p">Lorem ipsum dolor sit amet, consectetuer adipiscing elit. Aenean commodo ligula eget dolor. Aenean massa. Cum sociis natoque penatibus et magnis dis parturient montes.</p>

  <div class="abs feat" style="left:478px;top:767px">
    <svg width="34" height="34" viewBox="0 0 34 34" fill="none" stroke="#1e5fa0" stroke-width="1.4"><path d="M9 22a6 6 0 0 1 1-12 8 8 0 0 1 15 2 5 5 0 0 1-1 10z"/><circle cx="14" cy="27" r="2"/><circle cx="20" cy="27" r="2"/><path d="M14 22v3M20 22v3"/></svg>
    <span class="rule"></span><h4>CLOUD IP PBX</h4><p>Lorem ipsum dolor ipiscing elit. Aenean commodo ligula eget dolor.</p>
  </div>
  <div class="abs feat" style="left:727px;top:767px">
    <svg width="34" height="34" viewBox="0 0 34 34" fill="none" stroke="#1e5fa0" stroke-width="1.4"><rect x="4" y="10" width="18" height="16"/><rect x="14" y="5" width="16" height="12"/><path d="M8 30h12"/></svg>
    <span class="rule"></span><h4>MANAGE PROJECTS</h4><p>Lorem ipsum dolor ipiscing elit. Aenean commodo ligula eget dolor.</p>
  </div>
  <div class="abs feat" style="left:478px;top:865px">
    <svg width="34" height="34" viewBox="0 0 34 34" fill="none" stroke="#1e5fa0" stroke-width="1.4"><rect x="12" y="3" width="12" height="20" rx="2"/><path d="M6 20l6-4v14H6z"/></svg>
    <span class="rule"></span><h4>TEAM STATISTICS</h4><p>Lorem ipsum dolor ipiscing elit. Aenean commodo ligula eget dolor.</p>
  </div>
  <div class="abs feat" style="left:727px;top:865px">
    <svg width="34" height="34" viewBox="0 0 34 34" fill="none" stroke="#1e5fa0" stroke-width="1.4"><rect x="4" y="8" width="26" height="18" rx="2"/><path d="M8 14h18M8 20h18"/></svg>
    <span class="rule"></span><h4>UNLIMTED SHARING</h4><p>Lorem ipsum dolor ipiscing elit. Aenean commodo ligula eget dolor.</p>
  </div>
  <div class="abs feat" style="left:478px;top:976px">
    <svg width="34" height="34" viewBox="0 0 34 34" fill="none" stroke="#1e5fa0" stroke-width="1.4"><path d="M6 14h6l10-7v20l-10-7H6z"/><path d="M26 12a7 7 0 0 1 0 10"/></svg>
    <span class="rule"></span><h4>TEAM STATISTICS</h4><p>Lorem ipsum dolor ipiscing elit. Aenean commodo ligula eget dolor.</p>
  </div>
  <div class="abs feat" style="left:727px;top:976px">
    <svg width="34" height="34" viewBox="0 0 34 34" fill="none" stroke="#1e5fa0" stroke-width="1.4"><circle cx="17" cy="17" r="12"/><circle cx="17" cy="17" r="5"/><path d="M17 3v9M17 22v9M3 17h9M22 17h9"/></svg>
    <span class="rule"></span><h4>UNLIMTED SHARING</h4><p>Lorem ipsum dolor ipiscing elit. Aenean commodo ligula eget dolor.</p>
  </div>

  <section class="abs services" role="img" aria-label="Dark network background with glowing teal connected nodes">
    <h2>OUR SERVICES</h2>
    <div class="sub">With unlimited features that we offer, we promise it's possible to make everything that was impossible for you !</div>
  </section>

  <div class="abs svc" style="top:1314px">
    <svg width="26" height="26" viewBox="0 0 24 24"><path fill="#fff" d="M12 1l3.2 7 7.3.7-5.5 4.9 1.6 7.4L12 17.2 5.4 21l1.6-7.4L1.5 8.7 8.8 8z"/></svg>
    <h3>CLOUD IP PBX</h3>
    <p>A Multi-Tenant CloudPBX is able to handle multiple customers (tenants) with a single instance of the software. Even though every customer has a dedicated PBX, they all share the same switchyard instance ...</p>
  </div>
  <div class="abs svc" style="top:1425px">
    <svg width="26" height="26" viewBox="0 0 24 24"><path fill="#fff" d="M12 1l3.2 7 7.3.7-5.5 4.9 1.6 7.4L12 17.2 5.4 21l1.6-7.4L1.5 8.7 8.8 8z"/></svg>
    <h3>UNIFIED COMMUNICATIONS</h3>
    <p>Communicator is a Desktop &amp; Mobile Unified Communications application designed to provide business users with a set of features and benefits capable of transforming your company communications ...</p>
  </div>
  <div class="abs svc" style="top:1536px">
    <svg width="26" height="26" viewBox="0 0 24 24"><path fill="#fff" d="M12 1l3.2 7 7.3.7-5.5 4.9 1.6 7.4L12 17.2 5.4 21l1.6-7.4L1.5 8.7 8.8 8z"/></svg>
    <h3>INVOICE &amp; PAYMENT PLATFORM</h3>
    <p>Access Portal is a fully-featured telecom customer portal, designed for integration with one or many CloudPBX telephony switches. Access Portal has a friendly GUI that enables efficient, automated ...</p>
  </div>
  <div class="abs svc" style="top:1647px">
    <svg width="26" height="26" viewBox="0 0 24 24"><path fill="#fff" d="M12 1l3.2 7 7.3.7-5.5 4.9 1.6 7.4L12 17.2 5.4 21l1.6-7.4L1.5 8.7 8.8 8z"/></svg>
    <h3>DATA AND VOICE SERVICES</h3>
    <p>Ethernet – Symmetrical upload and downloads FibreNet – choose from three Internet speeds all with unlimited downloads Everything for your Business Communications Inbound Services, Call ...</p>
  </div>

  <div class="abs screens">
    <div class="tablet"><div class="scr" role="img" aria-label="Tablet screen with data centre and internet security illustration"></div></div>
    <div class="laptop"><div class="scr" role="img" aria-label="Screenshots of communicator app with voicemail, dialpad and contacts"></div></div>
  </div>

  <section class="abs cta">
    <h2>Available 24/7 for your help!</h2>
    <span class="btn">Call Now</span>
  </section>

  <footer class="abs footer">
    <div class="logo"><i></i>Halvora UC</div>
    <p class="about-f">Australia's Business Grade Unified Communications Company. White-Label Solution for all your Communication Needs.Liberating Businesses from Traditional Communications Systems.</p>
    <div class="legal"><span>PRIVACY POLICY</span><span>TERMS AND CONDITIONS</span></div>
    <div class="copy">Copyright © 2019 Rivet Halvora</div>

    <div class="col" style="left:553px">
      <h5>CATEGORIES</h5>
      <ul><li>Home</li><li>Testimonials</li><li>Team</li><li>Career</li><li>Contat</li></ul>
    </div>
    <div class="col dark" style="left:697px">
      <h5>COMMUNITY</h5>
      <ul><li>Blog</li><li>Discussions</li><li>Collections</li><li>Members</li><li>Products</li><li>Help Center</li></ul>
    </div>
    <div class="col" style="left:819px;top:50px">
      <h5 style="margin-left:3px;margin-bottom:10px">CONTACT US</h5>
      <div class="field">Name</div>
      <div class="field">Email Address</div>
      <div class="field">Subject</div>
      <div class="field msg">Message</div>
      <span class="btn send">Send</span>
    </div>
  </footer>

</div>
</body>
</html>
```